Innovative cost reduction consultant needs to build a group of technical advisors

We need to share our message and compassion for developing cost reduction in the automotive industry. We create opportunities for immediate innovation, by developing cost reduction solutions across suppliers with related process. Attached is an existing Power Point, but it needs improvement. Most of all, a good compelling story, why experts should join us.

Target Market(s)

Automotive industry, supply chain management

Industry/Entity Type

Automotive

Font styles to use
Serif
Sans Serif

Requirements
Must have
• Better visual graphics. There are a few, but they are not as visually appearing as I would like. A graphic with data should have a better visual impact then the ones that I created. I would like to share the message, that I am providing a solution for the automotive industry. The goal is to reduce costs and improve supplier and OEM relationships. The objective is to do so by creating opportunities for immediate innovation, by developing cost reduction solutions across suppliers with related processes. This message may need a visual graphic, which is missing from the presentation.
Nice to have
• Challenge my story and presentation. Does this make sense to you, and what is your opinions of the subject. Or, a relevant news source to validate the story.
Should not have
• I have not decided on the name of the venture or logo. So, let's just use my name as the source or writer. Derek Whitcombe, Cost Reduction Specialist. Thanks,

```html
<!DOCTYPE html>
<html lang="en">
<head>
<meta charset="utf-8">
<title>Derek Whitcombe — Cost Reduction Specialist</title>
<link rel="stylesheet" href="https://fonts.googleapis.com/css2?family=Crimson+Text:ital,wght@0,400;0,700;1,400&family=Montserrat:wght@400;600&display=swap">
<style>
  :root {
    --page: #ffffff;
    --ink: #1f1f1f;
    --brand-ink: #2a2a2a;
    --header-band: #e3eaf4;
    --rule-grey: #a9a9a9;
    --arrow-blue-light: #6aa8f0;
    --arrow-blue-dark: #2a73d9;
    --arrow-grey: #d6d6d6;
    --cash-green-light: #d9e0c6;
    --cash-green-mid: #9aa985;
    --cash-green-dark: #5d6b4a;
    --car-white: #fbfbfb;
    --car-grey: #c9ccd1;
    --car-shadow: #5a5e63;
    --tower-top: #e8dcc0;
    --tower-mid: #7f95ab;
    --tower-low: #27445f;
  }
  * { margin: 0; padding: 0; box-sizing: border-box; }
  html, body { width: 1200px; height: 676px; overflow: hidden; background: var(--page); }
  .slide { position: relative; width: 1200px; height: 676px; background: var(--page); color: var(--ink); font-family: "Crimson Text", Georgia, serif; }

  .brand { position: absolute; left: 24px; top: 28px; width: 170px; }
  .brand-name { font-family: "Montserrat", Arial, sans-serif; font-weight: 600; font-size: 12px; letter-spacing: 1.6px; text-transform: uppercase; color: var(--brand-ink); white-space: nowrap; }
  .brand-title { font-family: "Montserrat", Arial, sans-serif; font-weight: 400; font-size: 6.5px; letter-spacing: 1.3px; text-transform: uppercase; color: var(--brand-ink); margin-top: 3px; padding-left: 16px; white-space: nowrap; }

  .header-band { position: absolute; left: 208px; top: 8px; width: 992px; height: 66px; background: var(--header-band); border-left: 2px solid #f6f8fb; }
  .header-rule { position: absolute; left: 192px; top: 79px; width: 1008px; height: 4px; background: var(--rule-grey); }
  .footer-rule { position: absolute; left: 147px; top: 641px; width: 1053px; height: 5px; background: var(--rule-grey); }

  .tower-photo { position: absolute; left: 0; top: 80px; width: 147px; height: 596px;
    background: linear-gradient(180deg, var(--tower-top) 0%, #cfd2cf 22%, var(--tower-mid) 45%, var(--tower-low) 100%); }

  .photo { position: absolute; }
  .cash { background: linear-gradient(165deg, var(--cash-green-light) 0%, var(--cash-green-mid) 50%, var(--cash-green-dark) 100%); border-radius: 10px; }
  .cash-before { left: 348px; top: 116px; width: 182px; height: 104px; }
  .cash-after { left: 752px; top: 142px; width: 108px; height: 72px; }
  .car { background: linear-gradient(180deg, var(--car-white) 0%, #eceef0 45%, var(--car-grey) 80%, var(--car-shadow) 100%); border-radius: 48% 52% 16% 16% / 60% 60% 22% 22%; }
  .car-before { left: 262px; top: 214px; width: 180px; height: 96px; }
  .car-after { left: 826px; top: 228px; width: 132px; height: 70px; }

  .trend-arrows { position: absolute; left: 0; top: 0; width: 1200px; height: 676px; pointer-events: none; }
  .arrow-label { font-family: "Crimson Text", Georgia, serif; font-weight: 700; font-size: 19px; fill: #ffffff; }

  .headline { position: absolute; left: 250px; top: 352px; width: 780px; text-align: center; font-size: 37px; line-height: 44px; font-weight: 400; color: var(--ink); }

  .byline { position: absolute; right: 192px; top: 517px; text-align: right; font-size: 16px; line-height: 29px; color: var(--ink); }
  .byline-date { font-style: italic; }
  .byline-date sup { font-size: 10px; }

  .page-number { position: absolute; left: 1133px; top: 602px; font-size: 13px; color: #444; }
</style>
</head>
<body>
<main class="slide">
  <div class="brand">
    <div class="brand-name">Derek Whitcombe</div>
    <div class="brand-title">Cost Reduction Specialist</div>
  </div>

  <div class="header-band"></div>
  <div class="header-rule"></div>

  <div class="tower-photo" role="img" aria-label="Upward view of a glass office tower against a warm sky"></div>

  <div class="photo cash cash-before" role="img" aria-label="Large pile of banknote bundles: higher cost in 2010"></div>
  <div class="photo cash cash-after" role="img" aria-label="Smaller pile of banknote bundles: lower cost in 2016"></div>
  <div class="photo car car-before" role="img" aria-label="Large white sedan: the 2010 vehicle"></div>
  <div class="photo car car-after" role="img" aria-label="Smaller white sedan: the 2016 vehicle"></div>

  <svg class="trend-arrows" viewBox="0 0 1200 676" aria-hidden="true">
    <defs>
      <linearGradient id="forecastBlue" x1="0" y1="0" x2="0" y2="1">
        <stop offset="0" stop-color="#7fb5f3"/>
        <stop offset="1" stop-color="#2a73d9"/>
      </linearGradient>
    </defs>
    <polygon class="cost-arrow" points="530,164 706,164 706,154 730,178 706,202 706,192 530,192" fill="var(--arrow-grey)"/>
    <polygon class="forecast-arrow" points="442,236 788,236 788,222 824,258 788,294 788,280 442,280" fill="url(#forecastBlue)"/>
    <text class="arrow-label" x="461" y="264">2010</text>
    <text class="arrow-label" x="554" y="264">6-Year forecast</text>
    <text class="arrow-label" x="731" y="264">2016</text>
  </svg>

  <h1 class="headline">Creating opportunities for immediate innovation,<br>by developing cost reduction solutions across<br>suppliers with related processes.</h1>

  <div class="byline">
    <div class="byline-author">By Derek Whitcombe, Cost Reduction Specialist</div>
    <div class="byline-date">December 2<sup>nd</sup>, 2016</div>
  </div>

  <div class="page-number">2</div>
  <div class="footer-rule"></div>
</main>
</body>
</html>
```